Real Estate 24"x24" Sign, Business Card, Letter Head and Envelope

This is a 4 project contest. If we choose a design or designs we like from what you sent we are willing to pay an amount at our discretion for that design even if we don't like all your designs for the 4 projects. Please be creative. Attached are our logo files. Please message us with any questions. Thanks and Good Luck!
Project 1: QLTV Realty 24" x 24" yard sign
We want to use the same blue background in our logo for the sign where the logo in white font will be on. CMYK 100,80,0,0. Attached is a sample a local designer made for you to get an idea what we are looking for. In the sample, the website is way too big and the entire sign is very plain and not attractive looking plus blue color is wrong one. We want the logo on top as large as possible but keeping it proportionate and attractive looking buy not too big that it looks odd. The following information can go in white color background or same blue color background color. Our company colors are blue (as per logo), green (as per logo), and white. "Residential & Commercial" goes under the logo. Under that put our phone number "312-948-6051" as large as possible but still looks good and under that our website in much smaller but readable font "www.qltvrealty.com".
Project 2: Envelope
We have two version of the logo. Use one or both. Whatever looks best in your design. The envelope will be white. We only want on top left corner logo and underneath our mailing address: 5197 Larchmere Ave. Elmdale, IL 60093-1725. Maybe some creative decorative design at bottom of envelope will look nice
Project 3: Letter Head
We have two version of the logo. Use one or both. Whatever looks best in your design. We want the following information on the top of the letterhead. Logo, address: 5197 Larchmere Ave., Elmdale, IL 60093-1725, phone: 312-948-6051, fax: 312-682-9307 website www.qltvrealty.com, email: info@qltvrealty.com
Project 4: Business card
Use either logo. We need cards for two individuals. Information for Person 1: Dev Kulkarni, Managing Broker, Phone: 312-948-6051, Email: dev.kulkarni@qltvrealty.com. Person 2: Ajay Kulkarni Broker Phone: 312-519-8263 Email: ajay.kulkarni@qltvrealty.com. Add Address, Fax and website same as above letter head.

```html
<!DOCTYPE html>
<html lang="en">
<head>
<meta charset="utf-8">
<title>QLTV Realty Stationery</title>
<link href="https://fonts.googleapis.com/css2?family=Open+Sans:wght@400;600;700&display=swap" rel="stylesheet">
<style>
  :root {
    --brand-blue: #0d4da1;
    --brand-green: #6cbf44;
    --paper: #ffffff;
    --backdrop: #1e1e20;
    --ink-light: #ffffff;
  }
  * { margin: 0; padding: 0; box-sizing: border-box; }
  html, body {
    width: 1200px; height: 999px; overflow: hidden;
    background: var(--backdrop);
    font-family: "Open Sans", Arial, sans-serif;
  }
  .stage { position: relative; width: 1200px; height: 999px; }
  .sheet {
    position: absolute; background: var(--paper); overflow: hidden;
    box-shadow: 0 4px 14px rgba(0,0,0,.55);
  }
  .wordmark {
    position: absolute; display: flex; align-items: center; gap: 7px;
    color: var(--brand-blue); font-weight: 700; white-space: nowrap; letter-spacing: .5px;
  }
  .wordmark .mark-square { background: var(--brand-green); flex: none; }
  .band { position: absolute; left: 0; display: block; }
  .footer-text {
    position: absolute; color: var(--ink-light); font-size: 10.5px; line-height: 13px; font-weight: 600;
    white-space: nowrap;
  }
  .contact-line { display: flex; align-items: center; gap: 5px; }
  .contact-line svg { width: 9px; height: 9px; fill: var(--ink-light); flex: none; }

  /* letterhead */
  .letterhead { left: 98px; top: 65px; width: 674px; height: 871px; }
  .letterhead .wordmark { left: 32px; top: 36px; font-size: 28px; }
  .letterhead .wordmark .mark-square { width: 14px; height: 14px; }
  .letterhead .band { top: 747px; }

  /* envelope */
  .envelope { left: 386px; top: 487px; width: 713px; height: 315px; }
  .envelope .wordmark { left: 27px; top: 44px; font-size: 28px; }
  .envelope .wordmark .mark-square { width: 14px; height: 14px; }
  .envelope .band { top: 233px; }

  /* business cards */
  .card-front { left: 790px; top: 72px; width: 326px; height: 187px; }
  .card-front .wordmark { left: 50%; transform: translateX(-50%); top: 38px; font-size: 24px; }
  .card-front .wordmark .mark-square { width: 11px; height: 11px; }
  .card-front .band { top: 90px; }
  .card-name { position: absolute; left: 15px; top: 150px; color: var(--ink-light); }
  .card-name .person { font-size: 11.5px; font-weight: 700; }
  .card-name .role { font-size: 8px; font-weight: 600; margin-top: 1px; }
  .card-contacts { left: 195px; top: 134px; font-size: 8px; line-height: 11px; }
  .card-contacts .contact-line svg { width: 7px; height: 7px; }

  .card-back { left: 794px; top: 281px; width: 327px; height: 186px; }
  .card-back .wordmark { left: 50%; transform: translateX(-50%); top: 74px; font-size: 32px; }
  .card-back .wordmark .mark-square { width: 16px; height: 16px; }
</style>
</head>
<body>
<main class="stage">

  <!-- Letterhead -->
  <section class="sheet letterhead">
    <div class="wordmark"><span class="mark-square"></span>QLTV REALTY</div>
    <svg class="band" width="674" height="124" viewBox="0 0 674 124">
      <path d="M0 23 Q380 70 674 18 L674 124 L0 124Z" fill="var(--brand-blue)"/>
      <path d="M265 45 Q520 40 674 0 L674 12 Q520 49 265 45Z" fill="var(--brand-green)"/>
    </svg>
    <div class="footer-text" style="left:32px; top:823px;">
      <div>5197 Larchmere Ave.</div>
      <div>Elmdale, IL 60093-1725</div>
    </div>
    <div class="footer-text" style="left:277px; top:823px;">
      <div class="contact-line"><svg viewBox="0 0 10 10"><path d="M2 0h2l1 3-1.5 1a6 6 0 0 0 2.5 2.5L7 5l3 1v2c0 1-1 2-2 2A8 8 0 0 1 0 2c0-1 1-2 2-2z"/></svg>312-948-6051</div>
      <div class="contact-line"><svg viewBox="0 0 10 10"><path d="M2 0h6v3H2zM0 4h10v6H0zM3 6h4v2H3z"/></svg>312-682-9307</div>
    </div>
    <div class="footer-text" style="left:497px; top:823px;">
      <div class="contact-line"><svg viewBox="0 0 10 10"><path d="M0 3l5-3 5 3v7H0zM1 4l4 3 4-3"/></svg>info@qltvrealty.com</div>
      <div class="contact-line"><svg viewBox="0 0 10 10"><circle cx="5" cy="5" r="4.5" fill="none" stroke="#fff" stroke-width="1"/><path d="M0.5 5h9M5 .5v9" stroke="#fff" stroke-width="1"/></svg>qltvrealty.com</div>
    </div>
  </section>

  <!-- Envelope -->
  <section class="sheet envelope">
    <div class="wordmark"><span class="mark-square"></span>QLTV REALTY</div>
    <svg class="band" width="713" height="82" viewBox="0 0 713 82">
      <path d="M0 13 Q357 52 713 7 L713 15 Q357 56 0 19Z" fill="var(--brand-green)"/>
      <path d="M0 22 Q357 60 713 20 L713 82 L0 82Z" fill="var(--brand-blue)"/>
    </svg>
    <div class="footer-text" style="left:40px; top:281px;">5197 Larchmere Ave. Elmdale, IL 60093-1725</div>
  </section>

  <!-- Business card front -->
  <section class="sheet card-front">
    <div class="wordmark"><span class="mark-square"></span>QLTV REALTY</div>
    <svg class="band" width="326" height="97" viewBox="0 0 326 97">
      <path d="M0 18 Q160 38 326 14 L326 97 L0 97Z" fill="var(--brand-blue)"/>
      <path d="M128 33 Q250 29 326 2 L326 10 Q250 34 128 34Z" fill="var(--brand-green)"/>
    </svg>
    <div class="card-name">
      <div class="person">Dev Kulkarni</div>
      <div class="role">Managing Broker</div>
    </div>
    <div class="footer-text card-contacts">
      <div class="contact-line"><svg viewBox="0 0 10 10"><path d="M2 0h2l1 3-1.5 1a6 6 0 0 0 2.5 2.5L7 5l3 1v2c0 1-1 2-2 2A8 8 0 0 1 0 2c0-1 1-2 2-2z"/></svg>312-948-6051</div>
      <div class="contact-line"><svg viewBox="0 0 10 10"><path d="M2 0h6v3H2zM0 4h10v6H0zM3 6h4v2H3z"/></svg>312-682-9307</div>
      <div class="contact-line"><svg viewBox="0 0 10 10"><path d="M0 3l5-3 5 3v7H0z"/></svg>dev.kulkarni@qltvrealty.com</div>
      <div class="contact-line"><svg viewBox="0 0 10 10"><circle cx="5" cy="5" r="4.5" fill="none" stroke="#fff" stroke-width="1"/><path d="M0.5 5h9M5 .5v9" stroke="#fff" stroke-width="1"/></svg>qltvrealty.com</div>
    </div>
  </section>

  <!-- Business card back -->
  <section class="sheet card-back">
    <div class="wordmark"><span class="mark-square"></span>QLTV REALTY</div>
  </section>

</main>
</body>
</html>
```